依頼詳細
【依頼内容】
名刺デザイン

【納品ファイル形式】
AI形式で納品希望
デザイン確認用としてJPEGやPDFでも頂きたいです。

【仕上がりイメージ】
横型で、シンプル、スタイリッシュでかっこよく、洗練されたイメージの名刺

【その他】
ご提案時は、記載項目は×××や〇〇〇などのように文字が入ったイメージが持てるようにご提示ください。デザイン決定後、依頼させて頂くデザイナー様に個人情報をメッセージにてお送りします。
記載項目
【表面】ロゴ、会社名、役職、氏名、住所、電話番号、FAX、携帯番号、メールアドレス、HP、県知事番号、文字「To create imagination」

【裏面】事業内容、キャラクター

入れて頂きたいロゴとキャラクターを添付します。
上記の内容を入れた名刺のデザインを横型で作成お願い致します。
上記の表面、裏面への記載項目はデザインをされる過程で移動が必要と判断された場合、記載項目を移動しても問題ございません。柔軟なご対応とデザインをお願いできましたら有難いです。
希望イメージ
シンプル 複雑
単色 カラフル
暗い 明るい
日常 高級
遊び心 厳粛
未来的 伝統的
女性的 男性的
希望する色
納品ファイル
• イラストレーター形式 (.ai)
補足説明
■ 選んだ理由

シンプルなデザインながらも、明るい色で目を引く印象に残るものでした。

■ 提案者全員のお礼・コメント

この度は弊社コンペに多数のご提案ありがとうございました!
また機会がありましたら是非よろしくお願いします。

```html
<!DOCTYPE html>
<html lang="ja">
<head>
<meta charset="utf-8">
<title>Business Card – Front</title>
<link href="https://fonts.googleapis.com/css2?family=Noto+Sans+JP:wght@400;500&family=Montserrat:wght@400&display=swap" rel="stylesheet">
<style>
  :root {
    --backdrop: #eeeeee;
    --card: #ffffff;
    --band: #ad9d86;
    --ink: #1a1a1a;
    --on-band: #ffffff;
  }
  * { margin: 0; padding: 0; box-sizing: border-box; }
  html, body { width: 810px; height: 1200px; overflow: hidden; }
  body { background: var(--backdrop); position: relative; font-family: "Noto Sans JP", sans-serif; color: var(--ink); }
  .card {
    position: absolute; left: 45px; top: 382px;
    width: 720px; height: 436px; background: var(--card);
  }
  .brand-band {
    position: absolute; left: 0; top: 0; width: 280px; height: 100%;
    background: var(--band); color: var(--on-band); text-align: center;
  }
  .brand-mark { position: absolute; left: 104px; top: 118px; }
  .brand-name {
    position: absolute; left: 0; width: 100%; top: 208px;
    font-family: "Montserrat", sans-serif; font-size: 22px; letter-spacing: 0.5px;
  }
  .tagline {
    position: absolute; left: 0; width: 100%; bottom: 30px;
    font-family: "Montserrat", sans-serif; font-size: 12px; letter-spacing: 1.5px;
  }
  .details { position: absolute; left: 280px; top: 0; width: 440px; height: 100%; }
  .centered { position: absolute; left: 0; width: 100%; text-align: center; }
  .job-title { top: 34px; font-size: 13px; }
  .person-name { top: 52px; font-size: 32px; font-weight: 500; letter-spacing: 2px; line-height: 1.3; }
  .person-romaji { top: 98px; font-family: "Montserrat", sans-serif; font-size: 12px; letter-spacing: 0.5px; }
  .company { top: 140px; font-size: 16px; font-weight: 500; }
  .contact { top: 172px; font-size: 12.5px; line-height: 24px; }
  .license { top: 330px; font-size: 11.5px; }
</style>
</head>
<body>
  <main class="card">
    <section class="brand-band">
      <svg class="brand-mark" width="72" height="72" viewBox="0 0 72 72" aria-hidden="true">
        <circle cx="36" cy="36" r="33" fill="none" stroke="var(--on-band)" stroke-width="3"/>
      </svg>
      <p class="brand-name">Harbor Lane Homes</p>
      <p class="tagline">To create imagination</p>
    </section>
    <section class="details">
      <p class="centered job-title">代表取締役</p>
      <h1 class="centered person-name">名刺　一郎</h1>
      <p class="centered person-romaji">Ichiro Meishi</p>
      <p class="centered company">株式会社 森創建</p>
      <div class="centered contact">
        <p>〒000-0000 栃木県□□市□□□町1-23-4</p>
        <p>□□□□□□567</p>
        <p>TEL. 000-000-0000　FAX. 000-000-0000</p>
        <p>Mobile. 000-0000-0000</p>
        <p>E-mail k.morita@harborlane-h.jp</p>
        <p>https://www.□□□□□□□</p>
      </div>
      <p class="centered license">栃木県知事（0）第00000号</p>
    </section>
  </main>
</body>
</html>
```